Brindle's Botanic's. I make and sell organic bath & body products. Nourishing bath & body products. Products are soaps, scrubs, lip balms, bath salts, baby & mother products (belly balm, nipple balm, diaper balm, baby bath soak, chest rub,) . I use botanical and or herbs in all my recipes. I create my own recipes. I like muted colors...but I would like something that will get your attention. I like the colors green and brown, but open to any other colors. I would also like to get information about labels (different sizes for my products) I do like the pasley print and maybe even a cute owl.

Target Market(s)

women, pregnant and nursing women, women with children and men

Industry/Entity Type

Baby

Contact Information for Business Card

Mona Greeley
517-384-2706,mgreeley@tallowmail.example
mgreeley@tallowmail.example

Font styles to use
Other font styles liked:
• bree

Requirements
Must have
• Brindle's Botanic's, nourishing bath & body products. It needs to get a person attention. I would like to see cards that are hip and fun. I would also like to view cards that are classy. I do like muted colors but I do have an open mind (use any color you think would be right) So far a lot of the cards have had leaves....I really do not like that design.
Nice to have
• ???pasley in the background ?cute owl
Should not have
• leaves

```html
<!DOCTYPE html>
<html lang="en">
<head>
<meta charset="utf-8">
<title>Brindle's Botanic's</title>
<link href="https://fonts.googleapis.com/css2?family=Alfa+Slab+One&family=Arimo:wght@400;700&display=swap" rel="stylesheet">
<style>
  :root {
    --leaf-green: #8cc540;
    --pale-green: #c4e29a;
    --ink: #1a1a1a;
    --paper: #ffffff;
  }
  html, body {
    margin: 0;
    padding: 0;
    overflow: hidden;
    background: var(--paper);
  }
  .card {
    position: relative;
    width: 1200px;
    height: 703px;
    background: var(--paper);
    overflow: hidden;
    font-family: "Arimo", Arial, sans-serif;
  }
  .header-wave {
    position: absolute;
    top: 0;
    left: 0;
    width: 1200px;
    height: 190px;
  }
  .brand-name {
    position: absolute;
    top: 22px;
    right: 40px;
    margin: 0;
    font-family: "Alfa Slab One", Georgia, serif;
    font-weight: 400;
    font-size: 62px;
    color: var(--paper);
    letter-spacing: 1px;
  }
  .brief {
    position: absolute;
    top: 206px;
    left: 0;
    width: 1200px;
    margin: 0;
    text-align: center;
    font-size: 23.5px;
    line-height: 32px;
    color: var(--ink);
  }
  .contact-tag {
    position: absolute;
    top: 550px;
    left: 504px;
    width: 194px;
    height: 50px;
    border-radius: 6px;
    background: var(--leaf-green);
    color: var(--paper);
    font-weight: 700;
    font-size: 33px;
    line-height: 50px;
    text-align: center;
    letter-spacing: 1px;
  }
  .contact-bar {
    position: absolute;
    left: 0;
    bottom: 0;
    width: 1200px;
    height: 97px;
    background: var(--leaf-green);
    color: var(--paper);
    font-weight: 700;
    font-size: 35px;
    line-height: 97px;
    text-align: center;
    white-space: nowrap;
  }
</style>
</head>
<body>
<main class="card">
  <svg class="header-wave" viewBox="0 0 1200 190" aria-hidden="true">
    <path d="M0,0 H1200 V166 C1010,172 830,150 640,102 C450,54 250,26 0,42 Z" fill="var(--leaf-green)"/>
    <path d="M0,58 C250,44 450,72 640,120 C830,166 1010,186 1200,182" fill="none" stroke="var(--pale-green)" stroke-width="5"/>
  </svg>
  <h1 class="brand-name">Brindle's Botanic's</h1>

  <p class="brief">
    I make and sell organic bath &amp; body products. Nourishing bath &amp; body products.<br>
    Products are soaps, scrubs, lip balms, bath salts, baby &amp; mother products<br>
    (belly balm, nipple balm, diaper balm, baby bath soak, chest rub,) .<br>
    I use botanical and or herbs in all my recipes. I create my own recipes. I like<br>
    muted colors...but I would like something that will get your attention.<br>
    I like the colors green and brown, but open to any other colors. I would also<br>
    like to get information about labels (different sizes for my products) I do like<br>
    the pasley print and maybe even a cute owl.
  </p>

  <div class="contact-tag">CONTACT</div>
  <footer class="contact-bar">Mona Greeley 517-384-2706 mgreeley@tallowmail.example</footer>
</main>
</body>
</html>
```